Website setup with Cobalt Forge (childtheme is velmora theme)

hey there, my name is tobin and i would need a website. Quillon Framework, I use the velmora theme. I would like to say goodbye to the eye-catching website with a nice menu. I like to send you some example from websites I like. Https://dawnreachhabits.com/about/ https://dawnreachhabits.com The main tabs on the top should be "About", "Blog", "Video", "Resources" on the right / blog /

Number of Pages Required

1 page

Colors
0493ce
fbee3d
faa54b

```html
<!DOCTYPE html>
<html lang="en">
<head>
<meta charset="utf-8">
<title>Build Your Life — Dawnreach Habits</title>
<link href="https://fonts.googleapis.com/css2?family=Montserrat:wght@600;700;800&family=Open+Sans:wght@400;600;700&display=swap" rel="stylesheet">
<style>
:root{
  --blue:#0493ce;
  --yellow:#fbee3d;
  --orange:#faa54b;
  --orange-deep:#f5872a;
  --ink:#222428;
  --dark:#1f2126;
  --text:#555;
  --light:#f1f2f4;
  --panel:#f4f5f7;
  --white:#fff;
  --head:'Montserrat',sans-serif;
  --body:'Open Sans',sans-serif;
}
*{box-sizing:border-box;margin:0;padding:0}
html,body{width:1200px;height:4712px;overflow:hidden}
body{font-family:var(--body);color:var(--text);background:var(--white);position:relative}
section,header,footer{position:absolute;left:0;width:1200px;overflow:hidden}
.abs{position:absolute}
.btn{position:absolute;background:var(--orange-deep);color:var(--white);font-family:var(--head);font-weight:700;font-size:17px;letter-spacing:.5px;text-transform:uppercase;display:flex;align-items:center;justify-content:center;border-radius:3px;white-space:nowrap}
.photo{position:absolute}

/* header */
.site-header{top:0;height:94px;background:var(--dark)}
.brand{position:absolute;left:84px;top:32px;font-family:var(--head);font-weight:800;font-size:24px;color:var(--white);letter-spacing:.5px}
.header-social{position:absolute;right:58px;top:14px;display:flex;gap:14px}
.header-social span{width:14px;height:14px;border-radius:50%;background:#9aa0a8}
.main-nav{position:absolute;right:58px;top:54px;display:flex;gap:30px;align-items:center;font-family:var(--head);font-weight:600;font-size:14px;color:var(--white)}
.main-nav .current{color:var(--orange)}

/* share rail */
.share-rail{position:absolute;left:0;top:157px;width:36px;z-index:5}
.share-rail span{display:block;width:36px;height:36px;margin-bottom:3px;background:#555}

/* hero */
.hero{top:94px;height:471px;background:linear-gradient(180deg,#0b2d66 0%,#1e5aa8 50%,#0d3a78 100%)}
.hero .photo{left:0;top:0;width:1200px;height:471px;background:radial-gradient(ellipse at 50% 45%,rgba(90,140,210,.35),rgba(5,25,60,.5) 70%)}
.hero h1{position:absolute;left:0;width:1200px;top:210px;text-align:center;font-family:var(--head);font-weight:800;font-size:58px;color:var(--white)}
.hero p{position:absolute;left:320px;width:560px;top:288px;text-align:center;font-family:var(--head);font-weight:700;font-size:17px;line-height:1.4;color:var(--white)}
.hero .btn{left:458px;top:352px;width:236px;height:44px}
.slider-dots{position:absolute;right:110px;top:362px;display:flex;gap:8px}
.slider-dots span{width:18px;height:18px}

/* about */
.about{top:565px;height:622px;background:var(--white)}
.about h2{position:absolute;left:84px;top:45px;font-family:var(--head);font-weight:800;font-size:40px;color:var(--ink)}
.about .lead{position:absolute;left:84px;top:105px;font-family:var(--head);font-weight:700;font-size:20px;color:var(--blue)}
.about .copy{position:absolute;left:84px;width:560px;top:145px;font-size:13px;line-height:1.55}
.about .copy p{margin-bottom:14px}
.about .btn{left:84px;top:408px;width:210px;height:46px}
.about .photo{left:690px;top:15px;width:510px;height:490px;background:linear-gradient(160deg,#e9edf2,#c9d0d8 60%,#aeb6c0)}
.play{position:absolute;left:905px;top:236px;width:70px;height:70px;border-radius:50%;background:rgba(255,255,255,.55)}
.stats{position:absolute;left:182px;top:503px;display:flex}
.stat{width:206px;height:62px;display:flex;align-items:center;justify-content:center;gap:14px;color:var(--white);font-family:var(--head);font-weight:800;font-size:22px}
.stat i{width:22px;height:22px;background:rgba(255,255,255,.85);border-radius:3px}

/* finances */
.finances{top:1187px;height:493px;background:var(--panel)}
.finances .photo{left:0;top:0;width:600px;height:493px;background:linear-gradient(135deg,#1c2a40,#4a5872 55%,#7f8ba0)}
.finances h2{position:absolute;left:612px;top:93px;width:520px;font-family:var(--head);font-weight:800;font-size:28px;line-height:1.25;color:var(--ink)}
.finances p{position:absolute;left:612px;top:190px;width:520px;font-size:13px;line-height:1.6}
.finances .btn{left:612px;top:365px;width:212px;height:46px}

/* goals */
.goals{top:1680px;height:817px;background:linear-gradient(180deg,#3d4046,#2f3236)}
.goals h2{position:absolute;left:0;width:1200px;top:82px;text-align:center;font-family:var(--head);font-weight:800;font-size:38px;color:var(--white)}
.goals .sub{position:absolute;left:0;width:1200px;top:132px;text-align:center;font-size:13px;color:#cfd2d6}
.legend{position:absolute;left:410px;top:300px;font-size:14px;color:var(--white);line-height:28px}
.legend div{display:flex;align-items:center;gap:10px}
.legend i{width:16px;height:16px}
.timeline{position:absolute;left:0;top:580px;width:1200px;height:237px;background:#1b2330}
.years{position:absolute;left:234px;top:70px;display:flex;gap:32px}
.year{display:flex;flex-direction:column;align-items:center;gap:16px;font-family:var(--head);font-weight:700;font-size:18px;color:var(--orange);width:60px;white-space:nowrap}
.year .dot{width:36px;height:36px;border-radius:50%;background:var(--orange);display:flex;align-items:center;justify-content:center}
.year.off .dot{background:#9ea3aa}
.year.wide{width:150px;margin-left:12px}

/* posts */
.posts{top:2497px;height:863px;background:var(--light)}
.posts h2{position:absolute;left:0;width:1200px;top:52px;text-align:center;font-family:var(--head);font-weight:800;font-size:38px;color:var(--ink)}
.tabs{position:absolute;left:0;width:1200px;top:122px;display:flex;justify-content:center;gap:26px;font-family:var(--head);font-weight:600;font-size:11px;color:#888;align-items:center}
.tabs .on{background:var(--orange-deep);color:var(--white);padding:5px 10px}
.card{position:absolute;top:198px;width:325px;height:535px;background:var(--white)}
.card .photo{left:0;top:0;width:325px;height:273px}
.card h3{position:absolute;left:18px;top:300px;width:290px;font-family:var(--head);font-weight:700;font-size:15px;line-height:1.35;color:var(--ink)}
.card p{position:absolute;left:18px;top:362px;width:290px;font-size:12px;line-height:1.55}
.card .btn{left:18px;top:470px;width:124px;height:34px;font-size:13px}
.blog-link{position:absolute;left:0;width:1200px;top:790px;text-align:center;font-family:var(--head);font-weight:700;font-size:17px;color:var(--blue)}

/* offer */
.offer{top:3360px;height:486px;background:linear-gradient(90deg,#dfe2e6,#f4f5f7)}
.offer .photo{left:0;top:0;width:440px;height:486px;background:linear-gradient(160deg,#c7ccd3,#9aa3ae)}
.ribbon{position:absolute;font-family:var(--head);font-weight:800;font-size:26px;color:var(--white);padding:10px 24px;transform:skewX(-12deg);white-space:nowrap}
.ribbon span{display:inline-block;transform:skewX(12deg)}
.offer p{position:absolute;left:510px;top:312px;width:520px;font-size:17px;line-height:1.5;color:var(--ink)}
.offer .btn{left:580px;top:385px;width:260px;height:50px}

/* partners */
.partners{top:3846px;height:189px;background:var(--white);display:flex;justify-content:center;align-items:center;gap:60px}
.partners span{height:44px;background:#cfd2d6;border-radius:4px}

/* cta */
.cta{top:4035px;height:268px;background:var(--blue);text-align:center}
.cta h2{position:absolute;left:0;width:1200px;top:50px;font-family:var(--head);font-weight:800;font-size:38px;color:var(--white)}
.cta p{position:absolute;left:330px;width:540px;top:110px;font-family:var(--head);font-weight:700;font-size:17px;line-height:1.4;color:var(--white)}
.cta .btn{left:450px;top:190px;width:300px;height:46px}

/* footer */
.site-footer{top:4303px;height:409px;background:#26282c;color:#cfd2d6}
.site-footer .about-text{position:absolute;left:128px;top:62px;width:420px;font-size:12px;line-height:1.6}
.follow{position:absolute;left:665px;top:62px;font-family:var(--head);font-weight:700;font-size:13px;color:var(--white)}
.follow-icons{position:absolute;left:665px;top:92px;display:flex;gap:14px}
.follow-icons span{width:18px;height:18px;border-radius:50%;background:#9aa0a8}
.foot-nav{position:absolute;left:0;width:1200px;top:266px;display:flex;justify-content:center;gap:30px;font-family:var(--head);font-weight:600;font-size:12px}
.copyright{position:absolute;left:0;width:1200px;top:336px;text-align:center;font-size:11px;color:#8a8e94}
</style>
</head>
<body>

<header class="site-header">
  <div class="brand">DAWNREACH HABITS</div>
  <div class="header-social"><span></span><span></span><span></span><span></span><span></span><span></span><span></span><span></span><span></span><span></span></div>
  <nav class="main-nav">
    <span>START HERE</span><span class="current">ABOUT</span><span>BLOG</span><span>VIDEOS</span><span>COURSES</span><span>RESOURCES</span>
    <svg width="20" height="20" viewBox="0 0 20 20"><circle cx="8" cy="8" r="6" fill="none" stroke="#fff" stroke-width="2"/><line x1="12.5" y1="12.5" x2="18" y2="18" stroke="#fff" stroke-width="2"/></svg>
  </nav>
</header>

<div class="share-rail">
  <span style="background:#fff"></span><span style="background:#3b5a98"></span><span style="background:#2aa3ef"></span><span style="background:#d9432f"></span><span style="background:#c8232c"></span><span style="background:#0a77b5"></span><span style="background:#1a8bd6"></span><span style="background:#333"></span><span style="background:#777"></span>
</div>

<section class="hero">
  <div class="photo" role="img" aria-label="Speaker in a suit in front of a blue city backdrop"></div>
  <h1>BUILD YOUR LIFE</h1>
  <p>DISCOVER WHICH ONLINE BUSINESS MODEL IS RIGHT FOR YOU AND START YOUR ONLINE BUSINESS TODAY.</p>
  <div class="btn">Get an income</div>
  <div class="slider-dots"><span style="background:var(--yellow)"></span><span style="background:var(--blue)"></span><span style="background:var(--orange)"></span></div>
</section>

<section class="about">
  <h2>ABOUT TOBIN</h2>
  <div class="lead">Hi, I'm Tobin and welcome to Dawnreach Habits.</div>
  <div class="copy">
    <p>I'm an internet entrepreneur, life and business coach, philanthropist, and world traveler with an obsession for mastering every area of my life, fulfilling my potential as a human being and making a difference in the lives of others.</p>
    <p>At 17 years old, I began my self-development journey and have since been obsessed with learning and growing in all areas of my life. I started Dawnreach Habits in 2012 as a way to help others commit to mastering every area of their lives through self-development, including health, fitness, emotions, mindset, relationships, financial freedom, passive income, starting an online business, and spirituality.</p>
  </div>
  <div class="btn">Learn more</div>
  <div class="photo" role="img" aria-label="Portrait of a smiling man in a dark suit with arms crossed"></div>
  <div class="play"></div>
  <div class="stats">
    <div class="stat" style="background:#d0312d"><i></i>542.8K</div>
    <div class="stat" style="background:#3b5a98"><i></i>72.7K</div>
    <div class="stat" style="background:#4a6f8e"><i></i>60.9K</div>
    <div class="stat" style="background:#2aa3ef"><i></i>19.0K</div>
  </div>
</section>

<section class="finances">
  <div class="photo" role="img" aria-label="Speaker on stage waving to a large audience"></div>
  <h2>FINANCES, WEALTH, PASSIVE INCOME</h2>
  <p>Whether that be helping you start and build your own online business, creating financial freedom, motivating you to pursue your goals and dreams, to being more productive, improving your health and fitness, or inspiring you to constantly improve yourself to be the best that you can be. My mission is to get you to wake up to the unlimited potential within you and achieve what you're truly capable of through self-development. Dawnreach Habits is designed to be a source of self-development, inspiration, and change for those who refuse to settle for anything less than an extraordinary life.</p>
  <div class="btn">Get an income</div>
</section>

<section class="goals">
  <h2>GOALS REPORTS</h2>
  <div class="sub">welcome to Dawnreach Habits</div>
  <svg class="abs" style="left:110px;top:140px" width="300" height="300" viewBox="0 0 300 300">
    <circle cx="150" cy="160" r="140" fill="#f07c14"/>
    <path d="M150 160 L150 20 A140 140 0 0 0 26 95 Z" fill="#f6a21e"/>
    <path d="M150 160 L26 95 A140 140 0 0 0 22 215 Z" fill="#f8b92a"/>
    <path d="M150 160 L22 215 A140 140 0 0 0 70 275 Z" fill="#fbc93a"/>
    <line x1="150" y1="160" x2="150" y2="20" stroke="#fff" stroke-width="2"/>
    <line x1="150" y1="160" x2="26" y2="95" stroke="#fff" stroke-width="2"/>
    <line x1="150" y1="160" x2="22" y2="215" stroke="#fff" stroke-width="2"/>
    <line x1="150" y1="160" x2="70" y2="275" stroke="#fff" stroke-width="2"/>
  </svg>
  <div class="legend">
    <div><i style="background:#f07c14"></i>Partner Sponsorship</div>
    <div><i style="background:#f6a21e"></i>Coaching</div>
    <div><i style="background:#f8b92a"></i>Affiliate Revenue</div>
    <div><i style="background:#fbc93a"></i>Inner Circle Club</div>
  </div>
  <svg class="abs" style="left:560px;top:215px" width="620" height="320" viewBox="0 0 620 320" font-family="Open Sans, sans-serif" text-anchor="middle">
    <polygon points="200,0 239,60 161,60" fill="#fff3d9"/>
    <polygon points="160,62 240,62 279,122 121,122" fill="#fde7b0"/>
    <polygon points="120,124 280,124 319,184 81,184" fill="#fbc93a"/>
    <polygon points="80,186 320,186 359,246 41,246" fill="#f8a42a"/>
    <polygon points="40,248 360,248 399,308 1,308" fill="#f07c14"/>
    <g font-size="11" fill="#333">
      <text x="200" y="42">Estate</text><text x="200" y="54">planning</text>
      <text x="200" y="89">Retirement</text><text x="200" y="102">planning</text>
    </g>
    <g font-size="13" fill="#333">
      <text x="200" y="159">Financial goal planning</text>
      <text x="200" y="221">Risk planning</text>
      <text x="200" y="283">Emergency planning</text>
    </g>
    <line x1="232" y1="36" x2="268" y2="36" stroke="#ccc"/>
    <text x="272" y="41" fill="#fff" font-size="16" text-anchor="start">Distribution phase</text>
    <line x1="282" y1="131" x2="308" y2="131" stroke="#ccc"/>
    <text x="313" y="136" fill="#fff" font-size="16" text-anchor="start">Accumulation phase</text>
    <line x1="345" y1="254" x2="371" y2="254" stroke="#ccc"/>
    <text x="376" y="259" fill="#fff" font-size="16" text-anchor="start">Protection phase</text>
  </svg>
  <div class="timeline">
    <div class="years">
      <div class="year"><span class="dot"><svg width="16" height="16" viewBox="0 0 16 16"><path d="M3 8 L7 12 L13 4" fill="none" stroke="#fff" stroke-width="2.5"/></svg></span>2018</div>
      <div class="year"><span class="dot"><svg width="16" height="16" viewBox="0 0 16 16"><path d="M3 8 L7 12 L13 4" fill="none" stroke="#fff" stroke-width="2.5"/></svg></span>2017</div>
      <div class="year"><span class="dot"><svg width="16" height="16" viewBox="0 0 16 16"><path d="M3 8 L7 12 L13 4" fill="none" stroke="#fff" stroke-width="2.5"/></svg></span>2016</div>
      <div class="year"><span class="dot"><svg width="16" height="16" viewBox="0 0 16 16"><path d="M3 8 L7 12 L13 4" fill="none" stroke="#fff" stroke-width="2.5"/></svg></span>2015</div>
      <div class="year off"><span class="dot"></span>2014</div>
      <div class="year off"><span class="dot"></span>2013</div>
      <div class="year off wide"><span class="dot"></span>1ST 365 DAYS</div>
    </div>
  </div>
</section>

<section class="posts">
  <h2>MOST RECENT POSTS</h2>
  <div class="tabs"><span class="on">ALL</span><span>CAREER &amp; MISSION</span><span>MOTIVATION &amp; INSPIRATION</span><span>PRODUCTIVITY &amp; TIME MANAGEMENT</span><span>ONLINE MARKETING</span><span>SOCIAL &amp; FUN</span></div>
  <article class="card" style="left:100px">
    <div class="photo" role="img" aria-label="Businessman looking at city towers" style="background:linear-gradient(180deg,#9fb4c8,#3e526a)"></div>
    <h3>HOW TO FIND YOURSELF WHEN YOU'RE FEELING LOST IN LIFE (7 WAYS)</h3>
    <p>Whether that be helping you start and build your own online business, creating financial freedom, motivating you to pursue your goals and dreams, to being more productive, a source of self-development, inspiration.</p>
    <div class="btn">Read more</div>
  </article>
  <article class="card" style="left:455px">
    <div class="photo" role="img" aria-label="Hand drawing a rising chart arrow" style="background:linear-gradient(160deg,#5a6068,#22262c)"></div>
    <h3>HOW TO FIND YOUR PURPOSE IN LIFE</h3>
    <p>Whether that be helping you start and build your own online business, creating financial freedom, motivating you to pursue your goals and dreams, to being more productive, a source of self-development, inspiration.</p>
    <div class="btn">Read more</div>
  </article>
  <article class="card" style="left:810px">
    <div class="photo" role="img" aria-label="Desk with calculator and paperwork" style="background:linear-gradient(160deg,#d8d2c8,#8c8276)"></div>
    <h3>HOW TO FIND YOURSELF WHEN YOU'RE FEELING LOST IN LIFE (7 WAYS)</h3>
    <p>Whether that be helping you start and build your own online business, creating financial freedom, motivating you to pursue your goals and dreams, to being more productive, a source of self-development, inspiration.</p>
    <div class="btn">Read more</div>
  </article>
  <div class="blog-link">CLICK HERE FOR THE BLOG &gt;&gt;</div>
</section>

<section class="offer">
  <div class="photo" role="img" aria-label="Smiling man in a suit with arms crossed"></div>
  <div class="ribbon" style="left:460px;top:100px;background:var(--orange-deep)"><span>WANT TO BUILD AN ONLINE</span></div>
  <div class="ribbon" style="left:480px;top:166px;background:var(--orange-deep)"><span>BUSINESS THAT MAKER MONEY?</span></div>
  <div class="ribbon" style="left:490px;top:232px;background:var(--blue)"><span>I'LL TEACH YOU HOW.</span></div>
  <p>I started Dawnreach Habits in 2012 as a way to help others commit to mastering every area of their lives</p>
  <div class="btn">Get instant access</div>
</section>

<section class="partners">
  <span style="width:170px"></span><span style="width:150px"></span><span style="width:130px"></span><span style="width:150px"></span><span style="width:120px"></span>
</section>

<section class="cta">
  <h2>BUILD YOUR LIFE</h2>
  <p>DISCOVER WHICH ONLINE BUSINESS MODEL IS RIGHT FOR YOU AND START YOUR ONLINE BUSINESS TODAY.</p>
  <div class="btn">Get instant access</div>
</section>

<footer class="site-footer">
  <p class="about-text">Dawnreach Habits delivers the self-development advice you need to improve and master every area of your life. We provide world-class content, training, and coaching to maximize the your potential in your personal and business life. Everything from physical fitness, to emotional mindset, to relationships, to your financial freedom blend together to turn you into an unstoppable extraordinary person with an unstoppable extraordinary life.</p>
  <div class="follow">FOLLOW US</div>
  <div class="follow-icons"><span></span><span></span><span></span><span></span><span></span><span></span><span></span><span></span><span></span><span></span></div>
  <nav class="foot-nav"><span>ABOUT</span><span>BLOG</span><span>VIDEO</span><span>RESOURCES</span><span>SEARCH</span></nav>
  <div class="copyright">COPYRIGHT © 2018 DAWNREACH HABITS INC.</div>
</footer>

</body>
</html>
```